Brisk Nook vending machines facebook page design

We need a facebook page design for our startup company - Brisk Nook. We are providing vending machines which allow arm length access to healthy foods and beverages at office spaces. You can check our website's about page for more details on what we actually do, you can also see the products we offer and our mission and values.
We are looking for something fresh, catchy that reminds for youth, freedom and happiness as this is what we believe our bodies feel when we feed them well. At the same time we are looking for simplicity. The background might be just white and the main colours - green and pink (those green and pink from our logo) It could be some picture, text, will be good if we have a vending machine in the design so people can connect the brand with the actual service we offer.
You can check our website, logo and one of our branding designs, so you can see what we have so far. We are not looking for something similar, but the FB design should however be consistent with our website.
Note that the vending machines are offered only to companies' office spaces. It will be great if you somehow imply this in the design.
Our slogan is "Food for good" it can also be used.
Our FB page: https://www.facebook.com/brisknook.example/
Target Market(s)
middle, big-sized European companies
office spaces
companies that have corporate social responsibility policies
Industry/Entity Type
It Company
Contact Information for Business Card
Name: Mila Voranska
Title: Business Development
email: mila.v@brisknook.example
mobile: +359 842 63 58 91
Would like to have the logo on focus + the slogan "Food for good". The colours should be white, pink, green. Minimalistic, stylish, trustworthy this is what people should feel when they grab one.
It could be from one of the sides to have green or pink as background (with the contact details) , and on the other white background and the logo
It can also be the slogan from the one side, and logo + contact details on the other. Or Logo + slogan and on the other - only the contact details.
Font styles to use
Requirements
Must have
- the logo, slogan
- must be very cool, fresh
- must remain a change, youth and freedom
Nice to have
- simple but really catchy and thoughtful design
Should not have
- too much pictures,
- chaotic colours, subjects, images
- too much colours

```html
<!DOCTYPE html>
<html lang="en">
<head>
<meta charset="utf-8">
<title>Brisk Nook – Food for Good</title>
<link rel="stylesheet" href="https://fonts.googleapis.com/css2?family=Lobster&family=Open+Sans:wght@400;700&display=swap">
<style>
  :root {
    --sky-light: #ecfdff;
    --sky-mid: #a6ecf5;
    --sky-deep: #4fc3d6;
    --leaf: #5aa33a;
    --leaf-dark: #3f8a26;
    --berry: #e2418c;
    --berry-dark: #b8246a;
    --ink: #2b2b2b;
    --white: #ffffff;
    --machine-dark: #1b1d22;
    --machine-blue: #2f8fd8;
  }
  * { margin: 0; padding: 0; box-sizing: border-box; }
  html, body { width: 1200px; height: 444px; overflow: hidden; }
  body { font-family: "Open Sans", Arial, sans-serif; }

  .cover {
    position: relative;
    width: 1200px;
    height: 444px;
    overflow: hidden;
    background: radial-gradient(ellipse 60% 75% at 52% 45%, var(--sky-light) 0%, var(--sky-mid) 55%, var(--sky-deep) 100%);
  }

  .side-band { position: absolute; left: 0; top: 0; width: 360px; height: 444px; }

  .produce-badge {
    position: absolute;
    left: 52px; top: 16px;
    width: 200px; height: 200px;
    border-radius: 50%;
    border: 6px solid var(--white);
    box-shadow: 0 0 0 5px var(--leaf);
    background: radial-gradient(circle at 35% 35%, #8cc63f 0%, #d8352a 55%, #e87a24 100%);
  }

  .brand-badge {
    position: absolute;
    left: 124px; top: 241px;
    width: 176px; height: 176px;
    border-radius: 50%;
    background: var(--white);
    border: 7px solid var(--leaf);
    display: flex;
    align-items: center;
    justify-content: center;
    gap: 8px;
  }
  .brand-badge .dot {
    width: 12px; height: 12px; border-radius: 50%; background: var(--leaf);
  }
  .brand-name {
    font-family: "Open Sans", Arial, sans-serif;
    font-weight: 700;
    font-size: 22px;
    line-height: 1.05;
    color: var(--berry);
    text-align: center;
    width: 100px;
  }

  .slogan {
    position: absolute;
    left: 395px; top: 28px;
    width: 340px;
    transform: rotate(-9deg);
    font-family: "Lobster", cursive;
    color: var(--berry);
    -webkit-text-stroke: 3px var(--white);
    paint-order: stroke fill;
    text-shadow: 3px 4px 6px rgba(120, 20, 70, 0.35);
    line-height: 0.9;
  }
  .slogan .line-food { display: block; font-size: 118px; }
  .slogan .line-for { display: block; font-size: 48px; margin-left: 52px; margin-top: -4px; }
  .slogan .line-good { display: block; font-size: 118px; margin-left: 82px; margin-top: -30px; }

  .note {
    position: absolute;
    left: 395px; top: 372px;
    width: 360px;
    text-align: center;
    font-size: 18px;
    line-height: 1.4;
    color: var(--ink);
  }

  .vending-machine {
    position: absolute;
    left: 853px; top: 20px;
    width: 275px; height: 385px;
    border-radius: 6px;
    background: linear-gradient(90deg, var(--machine-dark) 0%, #2a2e36 70%, var(--machine-blue) 72%, #6cc0ee 100%);
  }
  .machine-reflection {
    position: absolute;
    left: 853px; top: 405px;
    width: 275px; height: 39px;
    background: linear-gradient(180deg, rgba(27,29,34,0.25), rgba(27,29,34,0));
  }
</style>
</head>
<body>
  <main class="cover">
    <svg class="side-band" viewBox="0 0 360 444" aria-hidden="true">
      <path d="M0 0 H188 C192 160 262 310 350 444 H0 Z" fill="var(--leaf)"/>
    </svg>

    <div class="produce-badge" role="img" aria-label="Heart-shaped arrangement of fresh vegetables and fruit"></div>

    <div class="brand-badge">
      <span class="dot"></span>
      <span class="brand-name">Brisk Nook</span>
    </div>

    <h1 class="slogan">
      <span class="line-food">Food</span>
      <span class="line-for">for</span>
      <span class="line-good">Good</span>
    </h1>

    <p class="note">Vending Machines are offered only to companies' office spaces.</p>

    <div class="vending-machine" role="img" aria-label="Branded vending machine stocked with bottled drinks and juices"></div>
    <div class="machine-reflection" aria-hidden="true"></div>
  </main>
</body>
</html>
```